UI Graphics Design For Web Based Home Control

Hi,
Our company Kelvo Systems is looking for user interface graphics in form of *.psd for home control user interface for a real system which can be used on mobile and PC/MAC.
In Ideal solution, the same interface should be used on mobile, tablets, computers. It changes only to fit the size of the screen. The bigger the screen, the more options you have visible on same view. The user should get familiar interface logic with every device.
The design should have at least the following views covered:
1. Lights view
- List of rooms and lamps
- You can see the status and you can switch it on/off
2. Login view
- Logo (company logo attached)
- Username field
- Password field
3. Dashboard view
- Indicating and choosing home/not home
- Can go to lights view
- Can go to settings view
- Notification list
4. Settings view
- View and edit users
- View and edit lights
Show us your view of ideal home control UI :)
Updates
Time of the project extended by 10 days to receive more designs. If someone sees that the reward should be increased, please also provide the amount expected with the first design. We are willing to increase the amount paid if we see a good design.
Reason: We expect to receive more designs. We are willing to increase the reward if we see good and acceptable designs. Please provide the amount expected with the first design. Project will end with full designs available.
We added our input as an attachment how we see the UI logic. Please have a look into the file.
Reason: We are seeing some good designs. We increased the budget. We are still not where we expect.
Industry/Entity Type
It Company
Look and feel
Each slider illustrates characteristics of the customer's brand and the style your logo design should communicate.

```html
<!DOCTYPE html>
<html lang="en">
<head>
<meta charset="utf-8">
<title>Kelvo Systems – Lights</title>
<link href="https://fonts.googleapis.com/css2?family=Open+Sans:wght@400;700&display=swap" rel="stylesheet">
<style>
  :root {
    --bg: #151515;
    --glow: #4a4fc4;
    --panel: #262626;
    --panel-edge: #3a3a3a;
    --home: #2d2a22;
    --item: #333333;
    --item-active: #1f3d75;
    --note: #25332f;
    --text: #ffffff;
    --bulb-on: #f4f4f4;
    --bulb-off: #4a4a4a;
    --brand: #1d3f55;
  }
  * { box-sizing: border-box; margin: 0; padding: 0; }
  html, body { width: 1200px; height: 750px; overflow: hidden; }
  body {
    position: relative;
    font-family: "Open Sans", Arial, sans-serif;
    color: var(--text);
    background:
      radial-gradient(ellipse 330px 300px at 790px 90px, rgba(150,155,220,.75), rgba(60,60,190,.55) 45%, rgba(30,30,90,.25) 75%, transparent 100%),
      radial-gradient(ellipse 520px 420px at 800px 160px, rgba(40,40,150,.5), transparent 80%),
      var(--bg);
  }
  .sidebar {
    position: absolute; left: 15px; top: 15px; width: 405px; height: 720px;
    background: var(--panel); border: 1px solid var(--panel-edge); border-radius: 28px;
  }
  .home-tile {
    position: absolute; left: 15px; top: 15px; width: 405px; height: 112px;
    background: var(--home); border: 1px solid #45413a; border-radius: 28px;
  }
  .home-tile .label { position: absolute; left: 174px; top: 44px; font-size: 19px; font-weight: 700; }
  .icon { position: absolute; }
  .home-tile .icon { left: 52px; top: 36px; }
  .nav { position: absolute; left: 29px; top: 147px; width: 376px; list-style: none; }
  .nav-item {
    position: relative; height: 69px; margin-bottom: 8.5px;
    background: var(--item); border-radius: 8px;
  }
  .nav-item.is-active { background: var(--item-active); }
  .nav-item .label {
    position: absolute; left: 154px; top: 17px; font-size: 22px; font-weight: 700;
    text-shadow: 1px 2px 3px rgba(0,0,0,.7);
  }
  .nav-item .icon { left: 34px; top: 10px; }
  .icon-placeholder { width: 50px; height: 48px; border-radius: 10px; background: linear-gradient(#d98a5e, #4d7fb3); }
  .notification {
    position: absolute; left: 15px; top: 623px; width: 405px; height: 112px;
    background: var(--note); border: 1px solid #3b4945; border-radius: 28px;
    display: flex; align-items: center; justify-content: center; font-size: 19px;
  }
  .screen-title { position: absolute; left: 808px; top: 33px; transform: translateX(-50%); font-size: 22px; font-weight: 700; text-shadow: 1px 2px 3px rgba(0,0,0,.6); }
  .clock { position: absolute; left: 1063px; top: 37px; font-size: 17px; font-weight: 700; }
  .lamp-list { position: absolute; left: 618px; top: 195px; list-style: none; }
  .lamp { position: relative; height: 76.3px; width: 400px; }
  .lamp .name { position: absolute; left: 0; top: 10px; font-size: 21px; font-weight: 700; }
  .lamp .status { position: absolute; left: 319px; top: 14px; font-size: 21px; font-weight: 700; }
  .lamp .bulb { position: absolute; left: 168px; top: 0; }
  .brand {
    position: absolute; left: 975px; top: 670px; display: flex; align-items: center; gap: 10px;
    font-size: 26px; font-weight: 700; color: var(--brand);
  }
  .brand .mark { width: 14px; height: 14px; border-radius: 50%; background: var(--brand); }
</style>
</head>
<body>
  <aside class="sidebar" aria-hidden="true"></aside>

  <div class="home-tile">
    <svg class="icon" width="38" height="40" viewBox="0 0 38 40" aria-hidden="true">
      <path d="M19 3 L36 19 H31 V37 H7 V19 H2 Z" fill="#f1e6d4"/>
      <path d="M19 3 L36 19 H2 Z" fill="#c0492d"/>
      <rect x="16" y="24" width="7" height="13" fill="#b5502c"/>
    </svg>
    <span class="label">HOME</span>
  </div>

  <ul class="nav">
    <li class="nav-item is-active">
      <svg class="icon" width="40" height="52" viewBox="0 0 40 52" aria-hidden="true">
        <path d="M20 2a15 15 0 0 0-9 27c2 2 3 4 3 8h12c0-4 1-6 3-8A15 15 0 0 0 20 2z" fill="#f2f2f2" stroke="#bbb"/>
        <rect x="14" y="38" width="12" height="9" rx="2" fill="#888"/>
      </svg>
      <span class="label">Lights</span>
    </li>
    <li class="nav-item">
      <svg class="icon" width="52" height="48" viewBox="0 0 52 48" aria-hidden="true">
        <circle cx="16" cy="14" r="9" fill="none" stroke="#999" stroke-width="6" stroke-dasharray="4 3"/>
        <circle cx="34" cy="30" r="12" fill="none" stroke="#8a8a8a" stroke-width="7" stroke-dasharray="5 3"/>
        <circle cx="34" cy="30" r="5" fill="#555"/>
      </svg>
      <span class="label">Settings</span>
    </li>
    <li class="nav-item">
      <svg class="icon" width="54" height="50" viewBox="0 0 54 50" aria-hidden="true">
        <circle cx="13" cy="12" r="9" fill="#e8e8e8" stroke="#999"/>
        <path d="M19 18 L48 44 L44 48 L15 22 Z" fill="#bfbfbf"/>
        <rect x="2" y="2" width="10" height="8" rx="2" fill="#e05a6a"/>
      </svg>
      <span class="label">Security</span>
    </li>
    <li class="nav-item">
      <svg class="icon" width="46" height="46" viewBox="0 0 46 46" aria-hidden="true">
        <path d="M23 4 L43 22 H38 V42 H8 V22 H3 Z" fill="#efe3cf"/>
        <path d="M23 4 L43 22 H3 Z" fill="#b94a34"/>
        <rect x="20" y="29" width="7" height="13" fill="#a8472c"/>
      </svg>
      <span class="label">Houses</span>
    </li>
    <li class="nav-item">
      <svg class="icon" width="40" height="56" viewBox="0 0 40 56" aria-hidden="true">
        <rect x="10" y="0" width="22" height="54" fill="#f3f3f3"/>
        <rect x="13" y="3" width="16" height="48" fill="#3a2a22"/>
        <path d="M13 3 L22 7 V55 L13 51 Z" fill="#eaeaea"/>
      </svg>
      <span class="label">Doors</span>
    </li>
    <li class="nav-item">
      <div class="icon icon-placeholder" role="img" aria-label="Users icon"></div>
      <span class="label">Users</span>
    </li>
  </ul>

  <div class="notification">Your Notification will reflect here!</div>

  <h1 class="screen-title">Lights</h1>
  <div class="clock">12:00 am</div>

  <ul class="lamp-list">
    <li class="lamp">
      <span class="name">Lmap 1</span>
      <svg class="bulb" width="48" height="58" viewBox="0 0 48 58" aria-hidden="true"><circle cx="24" cy="22" r="22" fill="rgba(255,255,255,.18)"/><path d="M24 6a13 13 0 0 0-8 23c2 2 3 4 3 7h10c0-3 1-5 3-7A13 13 0 0 0 24 6z" fill="var(--bulb-on)"/><rect x="19" y="37" width="10" height="10" rx="2" fill="#999"/></svg>
      <span class="status">On</span>
    </li>
    <li class="lamp">
      <span class="name">Lmap 2</span>
      <svg class="bulb" width="48" height="58" viewBox="0 0 48 58" aria-hidden="true"><path d="M24 6a13 13 0 0 0-8 23c2 2 3 4 3 7h10c0-3 1-5 3-7A13 13 0 0 0 24 6z" fill="var(--bulb-off)"/><rect x="19" y="37" width="10" height="10" rx="2" fill="#333"/></svg>
      <span class="status">Off</span>
    </li>
    <li class="lamp">
      <span class="name">Lmap 3</span>
      <svg class="bulb" width="48" height="58" viewBox="0 0 48 58" aria-hidden="true"><circle cx="24" cy="22" r="22" fill="rgba(255,255,255,.18)"/><path d="M24 6a13 13 0 0 0-8 23c2 2 3 4 3 7h10c0-3 1-5 3-7A13 13 0 0 0 24 6z" fill="var(--bulb-on)"/><rect x="19" y="37" width="10" height="10" rx="2" fill="#999"/></svg>
      <span class="status">On</span>
    </li>
    <li class="lamp">
      <span class="name">Lmap 4</span>
      <svg class="bulb" width="48" height="58" viewBox="0 0 48 58" aria-hidden="true"><circle cx="24" cy="22" r="22" fill="rgba(255,255,255,.18)"/><path d="M24 6a13 13 0 0 0-8 23c2 2 3 4 3 7h10c0-3 1-5 3-7A13 13 0 0 0 24 6z" fill="var(--bulb-on)"/><rect x="19" y="37" width="10" height="10" rx="2" fill="#999"/></svg>
      <span class="status">On</span>
    </li>
    <li class="lamp">
      <span class="name">Lmap 5</span>
      <svg class="bulb" width="48" height="58" viewBox="0 0 48 58" aria-hidden="true"><path d="M24 6a13 13 0 0 0-8 23c2 2 3 4 3 7h10c0-3 1-5 3-7A13 13 0 0 0 24 6z" fill="var(--bulb-off)"/><rect x="19" y="37" width="10" height="10" rx="2" fill="#333"/></svg>
      <span class="status">Off</span>
    </li>
  </ul>

  <div class="brand"><span class="mark"></span>Kelvo Systems</div>
</body>
</html>
```